Redesign of Business Cards to Update them!

We want a full overhaul of our business cards! We have a design that is almost 5 years old and it needs to be updated to be current

Address is 437 Dunmore Lane Suite 14 Marden Falls CA 93512
PH: 9094718263
Zorlivo.com

Hours M-F 10AM-4PM
Sat and Sunday Closed

```html
<!DOCTYPE html>
<html lang="en">
<head>
<meta charset="utf-8">
<title>Zorlivo Business Cards</title>
<link href="https://fonts.googleapis.com/css2?family=Oswald:wght@500&family=Questrial&display=swap" rel="stylesheet">
<style>
  :root {
    --backdrop: #a9aeb0;
    --paper: #efefed;
    --ink: #1a1a1a;
    --ink-soft: #4a4a4a;
    --accent: #e3000f;
    --edge: #b3000c;
    --rule: #8c8c8c;
  }
  * { margin: 0; padding: 0; box-sizing: border-box; }
  html, body { width: 1200px; height: 824px; overflow: hidden; }
  body {
    background: var(--backdrop);
    display: flex;
    align-items: center;
    justify-content: center;
    gap: 60px;
    font-family: "Questrial", sans-serif;
  }
  .card {
    width: 525px;
    height: 300px;
    background: var(--paper);
    border-bottom: 6px solid var(--edge);
    position: relative;
  }
  .card-front {
    display: flex;
    align-items: center;
    justify-content: center;
  }
  .identity {
    text-align: right;
    padding-right: 22px;
    align-self: center;
    margin-top: -40px;
  }
  .identity-name {
    font-family: "Oswald", sans-serif;
    font-weight: 500;
    font-size: 22px;
    color: var(--accent);
    letter-spacing: 0.01em;
    line-height: 1.1;
    white-space: nowrap;
  }
  .identity-title {
    font-size: 15px;
    color: var(--ink);
  }
  .divider {
    width: 1px;
    height: 110px;
    background: var(--rule);
  }
  .contact {
    padding-left: 22px;
    font-size: 15px;
    line-height: 1.25;
    color: var(--ink-soft);
    white-space: nowrap;
  }
  .contact-address { margin-bottom: 10px; }
  .card-back {
    display: flex;
    flex-direction: column;
    align-items: center;
    justify-content: center;
    gap: 16px;
  }
  .brand {
    display: flex;
    align-items: center;
    gap: 14px;
  }
  .brand-dot {
    width: 34px;
    height: 34px;
    border-radius: 50%;
    background: var(--accent);
  }
  .brand-name {
    font-size: 46px;
    color: var(--ink);
    letter-spacing: 0.04em;
  }
  .hours {
    text-align: center;
    font-size: 13px;
    color: var(--ink);
    text-transform: uppercase;
    letter-spacing: 0.04em;
    line-height: 1.4;
  }
</style>
</head>
<body>
  <section class="card card-front">
    <div class="identity">
      <p class="identity-name">DANIEL REYES</p>
      <p class="identity-title">President</p>
    </div>
    <div class="divider"></div>
    <div class="contact">
      <p class="contact-address">437 Dunmore Lane<br>Suite 14<br>Marden Falls CA 93512</p>
      <p class="contact-phone">909-471-8263</p>
      <p class="contact-web">www.Zorlivo.com</p>
    </div>
  </section>

  <section class="card card-back">
    <div class="brand">
      <span class="brand-dot"></span>
      <span class="brand-name">Zorlivo</span>
    </div>
    <div class="hours">
      <p>Hours M-F 10AM-4PM</p>
      <p>Sat and Sunday Closed</p>
    </div>
  </section>
</body>
</html>
```